New, clean letterhead for law firm in Colorado using recently designed logo.

Professional letterhead for established law firm rebranding. We service high end clientele with mostly family law and personal injury cases. Need source files for future changes. Prefer logo at top, names of members and staff in left margin, contact info in footer.

Target Market(s)

High wealth individuals

Contact Information for Business Card

Need options for traditional and square two sided business cards

Font styles to use
Serif

Colors
0555a3

Requirements
Must have
• Our logo; blue, gray, and white; modern feel.
Should not have
• Images of people

```html
<!DOCTYPE html>
<html lang="en">
<head>
<meta charset="utf-8">
<title>Harlow Pennington Law — Business Cards</title>
<link rel="stylesheet" href="https://fonts.googleapis.com/css2?family=Cinzel:wght@500&family=Roboto:wght@400;500;700&display=swap">
<style>
  :root {
    --brand-blue: #0555a3;
    --blue-mid: #2f78bd;
    --blue-light: #4a96cc;
    --gray: #9b9b9b;
    --gray-text: #5e5e5e;
    --white: #ffffff;
    --backdrop: #1f1f1f;
  }
  * { margin: 0; padding: 0; box-sizing: border-box; }
  html, body { width: 1200px; height: 929px; overflow: hidden; }
  body {
    background: var(--backdrop);
    position: relative;
    font-family: "Roboto", sans-serif;
  }
  .card {
    position: absolute;
    width: 560px;
    height: 320px;
    border-radius: 16px;
    overflow: hidden;
  }
  .card--front {
    left: 60px; top: 90px;
    background: radial-gradient(circle at 65% 60%, var(--blue-light), var(--blue-mid) 55%, #2369b2);
    display: flex; align-items: center; justify-content: center;
  }
  .firm-name {
    font-family: "Cinzel", serif;
    font-weight: 500;
    text-align: center;
    letter-spacing: 2px;
    line-height: 1.35;
  }
  .card--front .firm-name { color: var(--white); font-size: 30px; }
  .card--back { left: 580px; top: 500px; background: var(--white); }
  .card--back .firm-name {
    position: absolute; right: 34px; top: 32px;
    color: var(--blue-mid); font-size: 19px;
  }
  .divider {
    position: absolute; left: 250px; right: 30px; top: 126px;
    height: 1px; background: var(--gray);
  }
  .person { position: absolute; left: 36px; top: 140px; }
  .person__name {
    color: var(--blue-mid); font-weight: 700; font-size: 19px; letter-spacing: 0.5px;
  }
  .person__title { color: var(--gray-text); font-weight: 500; font-size: 14px; margin-top: 2px; }
  .contacts { list-style: none; margin-top: 10px; }
  .contacts li {
    display: flex; align-items: center; gap: 8px;
    color: var(--gray-text); font-size: 13.5px; line-height: 20px;
  }
  .contacts svg { width: 13px; height: 13px; flex: none; fill: var(--blue-mid); }
  .address {
    position: absolute; right: 34px; top: 138px;
    text-align: right; font-size: 13.5px; line-height: 18px; color: var(--gray-text);
  }
  .address__firm { color: var(--blue-mid); }
  .wave { position: absolute; left: 0; bottom: 0; width: 560px; height: 320px; }
</style>
</head>
<body>
  <section class="card card--front" aria-label="Business card front">
    <p class="firm-name">Harlow Pennington<br>Law, LLC</p>
  </section>

  <section class="card card--back" aria-label="Business card back">
    <p class="firm-name">Harlow Pennington<br>Law, LLC</p>
    <div class="divider"></div>

    <div class="person">
      <p class="person__name">MARCUS ELLERY</p>
      <p class="person__title">Managing Director</p>
      <ul class="contacts">
        <li><svg viewBox="0 0 16 16"><path d="M3 1l3 3-2 2c1 2 3 4 5 5l2-2 3 3-2 3C7 14 2 9 1 3z"/></svg>555.204.7781</li>
        <li><svg viewBox="0 0 16 16"><path d="M1 3h14v10H1z M2 4l6 5 6-5" fill="none" stroke="#2f78bd" stroke-width="1.5"/></svg>info@harlowpennington.com</li>
        <li><svg viewBox="0 0 16 16"><circle cx="8" cy="8" r="7"/><path d="M5 4c2 1 1 3 3 3s1 3 3 4" stroke="#fff" stroke-width="1.3" fill="none"/></svg>www.harlowpennington.com</li>
      </ul>
    </div>

    <div class="address">
      <p class="address__firm">Harlow Pennington Law, LLC</p>
      <p>48 Cedar Ridge Lane,</p>
      <p>Boulder, CO 80302</p>
    </div>

    <svg class="wave" viewBox="0 0 560 320" preserveAspectRatio="none" aria-hidden="true">
      <path d="M0 302 C170 298 360 270 560 234 L560 320 L0 320 Z" fill="var(--brand-blue)" opacity="0.85"/>
      <path d="M30 290 C200 288 380 262 530 224" fill="none" stroke="var(--gray)" stroke-width="4" stroke-linecap="round"/>
    </svg>
  </section>
</body>
</html>
```